Wealth Management Business Card

We are a professional services consulting firm that specializes in high net worth individuals over $25,000,000, executives C-suite and above, closely held businesses owners, family offices and highly compensated employees.

Our focus is on risk mitigation and tax efficient strategies. Our clients take their risk on themselves and have a proven track record generating wealth. Our directive is to preserve and protect the wealth they’ve already created.

Our company Harrowgate Advisory is geared around five directives of asset protection:
1) Legal Structuring
2) Leverage & Financing
3) Risk Management - Asset Protection & Insurance, Trustee Work
4) Asset Management & Investing - Under www.qlvbrookfield.com
5) Tax Efficient Strategies

Our Company Mark is a Pentagon with a key in the middle. A pentagon is the most efficient defensive structure. Each point of a pentagon is equal distance front every point . Each side provides support to another and works together, which is the key to our clients success.

Our key colors are blue, black and silver.

We ‘re located in the Pacific Northwest with bi coastal and international clients. We have fewer, higher net worth clients and provide exceptional customer service. We do not do social media.

website is www.harrowgatepath.com

Target Market(s)

High End Clients

Contact Information for Business Card

extra thick

Font styles to use
Serif

Requirements
Must have
• Metalic foil for lettering.
Black Background on one side
White Background on the other
Horizontal Format Only
No Rounded corners
Not Marketing sales information on the card.
Nice to have
• imprinted texture on the card
Should not have
• lots of color

```html
<!DOCTYPE html>
<html lang="en">
<head>
<meta charset="utf-8">
<title>Harrowgate Advisory – Business Card</title>
<link href="https://fonts.googleapis.com/css2?family=Cinzel:wght@500&family=Lato:wght@400;900&display=swap" rel="stylesheet">
<style>
  :root {
    --backdrop: #d3d3cf;
    --card-white: #ffffff;
    --card-black: #050607;
    --navy: #14287a;
    --blue: #1f5fc4;
    --grey-text: #6b6d70;
    --silver: #c9ccd1;
    --pattern-tone: #1c1d20;
  }
  * { margin: 0; padding: 0; box-sizing: border-box; }
  html, body { width: 1200px; height: 801px; overflow: hidden; }
  body {
    background: var(--backdrop);
    display: flex;
    align-items: center;
    justify-content: center;
    gap: 40px;
    font-family: "Lato", Arial, sans-serif;
  }
  .card {
    width: 520px;
    height: 297px;
    position: relative;
    box-shadow: 0 10px 28px rgba(0,0,0,0.22);
  }
  /* Front */
  .card-front { background: var(--card-white); }
  .brand {
    position: absolute;
    left: 34px;
    top: 44px;
    display: flex;
    align-items: center;
    gap: 12px;
  }
  .brand-mark {
    width: 14px; height: 14px;
    background: var(--navy);
  }
  .brand-name {
    font-family: "Cinzel", Georgia, serif;
    font-weight: 500;
    font-size: 26px;
    letter-spacing: 1px;
    color: var(--navy);
  }
  .person {
    position: absolute;
    left: 34px;
    top: 150px;
  }
  .person-name {
    font-weight: 900;
    font-size: 21px;
    color: var(--navy);
    text-transform: uppercase;
    letter-spacing: -0.3px;
  }
  .person-title {
    font-size: 14px;
    color: var(--grey-text);
    margin-top: 2px;
  }
  .contact-list {
    position: absolute;
    left: 34px;
    top: 212px;
    list-style: none;
  }
  .contact-item {
    display: flex;
    align-items: center;
    gap: 10px;
    font-size: 13.5px;
    color: var(--grey-text);
    line-height: 22px;
  }
  .contact-icon { width: 13px; height: 13px; fill: var(--navy); }
  .address {
    position: absolute;
    right: 34px;
    bottom: 58px;
    text-align: left;
    font-size: 13.5px;
    line-height: 21px;
    color: var(--grey-text);
    font-style: normal;
  }
  /* Back */
  .card-back { background: var(--card-black); overflow: hidden; }
  .back-pattern {
    position: absolute; inset: 0;
    background: radial-gradient(ellipse at 70% 30%, var(--pattern-tone) 0%, var(--card-black) 70%);
  }
  .back-brand {
    position: absolute;
    inset: 0;
    display: flex;
    align-items: center;
    justify-content: center;
    gap: 12px;
  }
  .back-brand .brand-mark { background: var(--silver); }
  .back-brand .brand-name { color: var(--silver); font-size: 22px; }
</style>
</head>
<body>
  <section class="card card-front">
    <div class="brand">
      <span class="brand-mark"></span>
      <span class="brand-name">Harrowgate Advisory</span>
    </div>
    <div class="person">
      <div class="person-name">Evan Marlowe</div>
      <div class="person-title">Founder &amp; CEO</div>
    </div>
    <ul class="contact-list">
      <li class="contact-item">
        <svg class="contact-icon" viewBox="0 0 16 16"><path d="M3.5 1.5l2.5 3-1.6 1.6a9 9 0 0 0 5.5 5.5L11.5 10l3 2.5-1.5 2.5C7 15 1 9 1 3z"/></svg>
        (503) 555-0148
      </li>
      <li class="contact-item">
        <svg class="contact-icon" viewBox="0 0 16 16"><path d="M1 3h14v10H1z M2 4l6 5 6-5" fill="none" stroke="#14287a" stroke-width="1.6"/></svg>
        info@harrowgatepath.com
      </li>
      <li class="contact-item">
        <svg class="contact-icon" viewBox="0 0 16 16"><g fill="none" stroke="#14287a" stroke-width="1.4"><circle cx="8" cy="8" r="6.5"/><ellipse cx="8" cy="8" rx="3" ry="6.5"/><path d="M1.5 8h13"/></g></svg>
        www.harrowgatepath.com
      </li>
    </ul>
    <address class="address">
      418 Alder Row, Suite 120,<br>
      Cedar Hollow, OR 97999
    </address>
  </section>

  <section class="card card-back">
    <div class="back-pattern" role="img" aria-label="Faint tonal brand pattern on black"></div>
    <div class="back-brand">
      <span class="brand-mark"></span>
      <span class="brand-name">Harrowgate Advisory</span>
    </div>
  </section>
</body>
</html>
```